Stonefield Partners Business Card Design

We are looking for a new business card design, we are not happy with our current design. We are a boutique management consulting firm and our clients are typically fortune 500 companies.

I have attached the current front and back that we have as well as a version of our logo that can be used. I am trying to get a higher resolution version of the logo file to upload to the project.

Target Market(s)

Fortune 500 companies are our primary client base. Financial services, life sciences, pharmaceuticals and telecom companies are

Industry/Entity Type

Management Consulting

Contact Information for Business Card

We are trying to communicate a high degree of professionalism, a somewhat minimalist perhaps with some air of whimsy (without overdoing it). Attached is the current design, front and back as well as logos. I like the current back of the card and assume we will keep the phrase the same.

From a color palette perspective, I prefer to stay with a gray scale as they are today.

Font styles to use
Sans Serif

Colors
1b1b1b
474747
ffffff

Requirements
Must have
• Two sided business card design. File format should be something that can be used outside of Photoshop like MS Publisher so that they can be edited with personal information.
• Font should be calibri or something very similar and should be available within MS Office
Should not have
• No other logos or graphics outside of the logo provided.

```html
<!DOCTYPE html>
<html lang="en">
<head>
<meta charset="utf-8">
<title>Stonefield Partners Business Card</title>
<link href="https://fonts.googleapis.com/css2?family=Carlito:wght@400;700&display=swap" rel="stylesheet">
<style>
  :root {
    --backdrop: #2e2a27;
    --card: #1b1b1b;
    --card-edge: #262626;
    --mid-gray: #474747;
    --mark-gray: #a6a6a6;
    --white: #ffffff;
  }
  * { box-sizing: border-box; margin: 0; padding: 0; }
  html, body {
    width: 1200px;
    height: 787px;
    overflow: hidden;
    background: var(--backdrop);
    font-family: "Carlito", "Calibri", sans-serif;
    color: var(--white);
  }
  .stage {
    width: 1200px;
    height: 787px;
    display: flex;
    align-items: center;
    justify-content: center;
    gap: 48px;
  }
  .card {
    width: 540px;
    height: 309px;
    background: var(--card);
    border: 1px solid var(--card-edge);
    border-radius: 4px;
    position: relative;
    box-shadow: 0 14px 30px rgba(0,0,0,0.45);
  }

  /* Front */
  .card-front { padding: 46px 40px 0 52px; }
  .wordmark {
    display: flex;
    align-items: center;
    gap: 12px;
    color: var(--mark-gray);
    font-weight: 700;
    font-size: 46px;
    line-height: 1;
    margin-left: 40px;
  }
  .wordmark-dot {
    width: 30px;
    height: 30px;
    border-radius: 50%;
    background: var(--mark-gray);
    flex: none;
  }
  .tagline {
    margin-top: 40px;
    font-weight: 700;
    font-size: 25px;
    line-height: 1.15;
    text-align: center;
  }
  .website {
    margin-top: 16px;
    font-size: 14px;
    letter-spacing: 1.5px;
    text-align: center;
    color: #d9d9d9;
  }

  /* Back */
  .card-back { display: flex; align-items: stretch; }
  .brand-panel {
    width: 220px;
    display: flex;
    flex-direction: column;
    align-items: center;
    justify-content: center;
    gap: 16px;
  }
  .brand-circle {
    width: 120px;
    height: 120px;
    border-radius: 50%;
    background: var(--white);
  }
  .brand-name {
    font-size: 26px;
    font-weight: 700;
    color: var(--white);
  }
  .divider {
    width: 1px;
    margin: 34px 0;
    background: var(--mid-gray);
  }
  .contact {
    padding: 30px 0 0 22px;
    font-size: 16px;
    line-height: 1.18;
  }
  .contact-name { font-weight: 700; font-size: 19px; }
  .contact-role { margin-bottom: 10px; }
  .contact-address { margin-bottom: 8px; }
  .contact-line { display: flex; align-items: center; gap: 8px; }
  .contact-line svg { width: 13px; height: 13px; flex: none; }
</style>
</head>
<body>
<main class="stage">
  <section class="card card-front" aria-label="Card front">
    <div class="wordmark"><span class="wordmark-dot"></span>Stonefield</div>
    <p class="tagline">The preferred choice<br>for leadership's top priorities</p>
    <p class="website">www.StonefieldPartners.com</p>
  </section>

  <section class="card card-back" aria-label="Card back">
    <div class="brand-panel">
      <span class="brand-circle"></span>
      <span class="brand-name">Stonefield</span>
    </div>
    <div class="divider"></div>
    <div class="contact">
      <p class="contact-name">Jordan Hale</p>
      <p class="contact-role">Los Angeles Office<br>Managing Director</p>
      <p class="contact-address">Stonefield Partners, Inc.<br>Headquarters<br>210 Harlow Street<br>Suite 103<br>Cedar Bay, WA 98000</p>
      <p class="contact-line">
        <svg viewBox="0 0 16 16" aria-hidden="true"><path fill="#ffffff" d="M3.6 1.2l2.3 2.6-1.3 1.9c.9 2 2.6 3.8 4.7 4.8l1.9-1.3 2.6 2.3-1.2 2.3C7.2 14.3 1.8 8.9 1.3 2.4z"/></svg>
        555.014.2297
      </p>
      <p class="contact-line">
        <svg viewBox="0 0 16 16" aria-hidden="true"><rect x="1" y="3" width="14" height="10" fill="#ffffff"/><path d="M1 3.5l7 5 7-5" fill="none" stroke="#1b1b1b" stroke-width="1.4"/></svg>
        jhale@stonefieldpartners.com
      </p>
    </div>
  </section>
</main>
</body>
</html>
```